Hairdressing Salon called; Velvet Tress. Style Lives Here

Velvet Tress
We Love Hair
418 Penrose Lane Birch Vale
5183742
Business card not to fussy.
I would like it to be a Black background with White and/or Grey lettering.

I really like the business card attached, so if the front looked like this I would be really happy, but would also like my address and phone number on the front.

On the back I would like two options of
1: reward card; buy any Haircare product over $20 on any visit and on the tenth product receive a complimentry Treatment and
2: appointment times and date

Industry/Entity Type

Business

Contact Information for Business Card

Velvet Tress
We Love Hair
5183742
418 Penrose Lane, Birch Vale
This must all be included on the front of the card

Font styles to use
Serif
Decorative
Script

Colors
1b1b1b
757575
ffffff

Requirements
Must have
• My phone number and address
Should not have
• Pictures on the front

```html
<!DOCTYPE html>
<html lang="en">
<head>
<meta charset="utf-8">
<title>Velvet Tress — Business Card</title>
<link rel="stylesheet" href="https://fonts.googleapis.com/css2?family=Tinos:wght@400;700&display=swap">
<style>
  :root {
    --page: #ffffff;
    --card: #1f1b1b;
    --ink: #ffffff;
    --ink-soft: #e4e2e2;
    --line: #e8e6e6;
    --damask-a: #4a4646;
    --damask-b: #2a2626;
  }
  * { margin: 0; padding: 0; box-sizing: border-box; }
  html, body {
    width: 1200px; height: 900px; overflow: hidden;
    background: var(--page);
    font-family: "Tinos", "Times New Roman", serif;
  }
  .canvas { position: relative; width: 1200px; height: 900px; }
  .card {
    position: absolute; left: 221px; width: 759px; height: 420px;
    background: var(--card); color: var(--ink); overflow: hidden;
  }
  .card--front { top: 25px; }
  .card--back { top: 463px; }
  .card__damask {
    position: absolute; left: 130px; top: 30px; width: 500px; height: 330px;
    background: radial-gradient(ellipse at center, var(--damask-a) 0%, var(--damask-b) 55%, rgba(31,27,27,0) 75%);
    opacity: .55;
  }
  .card__frame { position: absolute; inset: 0; }
  .card__ornament {
    position: absolute; left: 287px; top: 38px; width: 188px; height: 76px;
    background: radial-gradient(ellipse at center, #d8d6d6 0%, #8a8686 50%, rgba(31,27,27,0) 72%);
  }
  .brand-name {
    position: absolute; left: 0; right: 0; top: 136px;
    text-align: center; font-size: 50px; line-height: 1; color: var(--ink-soft);
  }
  .contact {
    position: absolute; left: 0; right: 0; top: 206px;
    text-align: center; font-size: 19px; color: var(--ink-soft);
  }
  .contact__line { display: block; height: 29px; line-height: 29px; }
  .contact__line--phone { margin-top: 6px; }
  .tagline {
    position: absolute; left: 0; right: 0; top: 325px;
    text-align: center; font-size: 36px; line-height: 40px; color: var(--ink-soft);
  }
  .offers {
    position: absolute; left: 84px; top: 154px; list-style: none;
    font-size: 20px; color: var(--ink-soft);
  }
  .offers__title { font-weight: 700; line-height: 26px; }
  .offers__detail { padding-left: 25px; line-height: 27px; }
  .offers__item + .offers__item { margin-top: 16px; }
</style>
</head>
<body>
<main class="canvas">

  <section class="card card--front">
    <div class="card__damask" role="img" aria-label="Faint grey damask pattern behind the text"></div>
    <svg class="card__frame" width="759" height="420" viewBox="0 0 759 420" aria-hidden="true">
      <g fill="none" stroke="var(--line)" stroke-width="3">
        <path d="M40 20 H719 A18 18 0 0 0 737 38 V382 A18 18 0 0 0 719 400 H40 A18 18 0 0 0 22 382 V38 A18 18 0 0 0 40 20 Z"/>
        <path d="M120 106 H288 M472 106 H640"/>
        <path d="M120 351 H237 M521 351 H640"/>
      </g>
      <g fill="var(--line)">
        <circle cx="28" cy="23" r="7"/><circle cx="729" cy="23" r="7"/>
        <circle cx="28" cy="395" r="7"/><circle cx="729" cy="395" r="7"/>
        <circle cx="120" cy="106" r="5"/><circle cx="640" cy="106" r="5"/>
        <circle cx="120" cy="351" r="5"/><circle cx="640" cy="351" r="5"/>
      </g>
    </svg>
    <div class="card__ornament" role="img" aria-label="White filigree flourish ornament"></div>
    <h1 class="brand-name">Velvet Tress</h1>
    <p class="contact">
      <span class="contact__line">418 Penrose Lane Birch Vale</span>
      <span class="contact__line">5183742</span>
      <span class="contact__line contact__line--phone">Phone: +612845 3390 71166</span>
    </p>
    <p class="tagline">We Love Hair</p>
  </section>

  <section class="card card--back">
    <div class="card__damask" role="img" aria-label="Faint grey damask pattern behind the text"></div>
    <svg class="card__frame" width="759" height="420" viewBox="0 0 759 420" aria-hidden="true">
      <g fill="none" stroke="var(--line)" stroke-width="3">
        <path d="M40 20 H719 A18 18 0 0 0 737 38 V382 A18 18 0 0 0 719 400 H40 A18 18 0 0 0 22 382 V38 A18 18 0 0 0 40 20 Z"/>
        <path d="M120 106 H288 M472 106 H640"/>
        <path d="M120 351 H237 M521 351 H640"/>
      </g>
      <g fill="var(--line)">
        <circle cx="28" cy="23" r="7"/><circle cx="729" cy="23" r="7"/>
        <circle cx="28" cy="395" r="7"/><circle cx="729" cy="395" r="7"/>
        <circle cx="120" cy="106" r="5"/><circle cx="640" cy="106" r="5"/>
        <circle cx="120" cy="351" r="5"/><circle cx="640" cy="351" r="5"/>
      </g>
    </svg>
    <div class="card__ornament" role="img" aria-label="White filigree flourish ornament"></div>
    <ol class="offers">
      <li class="offers__item">
        <p class="offers__title">1. Reward card:</p>
        <p class="offers__detail">buy any Haircare product over $20 on any visit<br>and on the tenth product receive a complimentry Treatment</p>
      </li>
      <li class="offers__item">
        <p class="offers__title">2. Appointment times and date</p>
      </li>
    </ol>
    <p class="tagline">We Love Hair</p>
  </section>

</main>
</body>
</html>
```